Criação de Capa para Facebook para Consultoria de Negócios
A empresa queria:
" DANDO SUPORTE TECNICO, COMERCIAL, OPERACIONAL, TREINAMENTO E PALESTRAS MOTIVACIONAIS, BEM COMO A ELABORAÇAO DE PLANOS DE NEGOCIOS, ESTRUTURAÇAO, REESTRUTURAÇAO DE EMPRESAS DE TODOS OS PORTES, ALÉM DE ASSESSORARAMOS TAMBEM NA AREA DE RECURSOS HUMANOS. NAS AREAS DE SEGURO, FINANCEIRA, INDUSTRIAL, COMERCIAL, ETC. PRESTANDO CONSULTORIA EMPRESARIAL NA AREA DE SEGUROS, PLANOS DE NEGOCIOS, TREINAMENTO, RH, ASSESSORIA DE MARKETING, REESTRURAÇAO OPERACIONAL ETC. "

```html
<!DOCTYPE html>
<html lang="pt-BR">
<head>
<meta charset="UTF-8">
<title>Veltra Consultoria – Capa Facebook</title>
<link href="https://fonts.googleapis.com/css2?family=Arimo:wght@400;700&display=swap" rel="stylesheet">
<style>
  :root {
    --stage: #3f3f3f;
    --navy: #14325c;
    --white: #ffffff;
    --ink: #111111;
    --ring: #1a1a1a;
    --photo-light: #e9edf2;
    --photo-dark: #8a97a8;
  }
  * { box-sizing: border-box; margin: 0; padding: 0; }
  html, body { width: 1200px; height: 1200px; overflow: hidden; }
  body {
    background: var(--stage);
    font-family: "Arimo", Arial, sans-serif;
    position: relative;
  }
  .cover {
    position: absolute;
    left: 67px; top: 355px;
    width: 1061px; height: 521px;
    background: var(--white);
    overflow: hidden;
  }
  .top-band {
    position: absolute; left: 0; top: 0;
    width: 100%; height: 41px;
    background: var(--navy);
  }
  .top-band__brand {
    position: absolute; right: 12px; top: 12px;
    display: flex; align-items: center; gap: 8px;
    color: var(--white); font-weight: 700; font-size: 14px;
  }
  .top-band__square {
    width: 20px; height: 20px;
    background: var(--white);
    border: 2px solid var(--ink);
  }
  .panel { position: absolute; left: 0; top: 41px; width: 1061px; height: 401px; }
  .photo {
    position: absolute;
    left: 797px; top: 77px;
    width: 384px; height: 384px;
    border-radius: 50%;
    background: radial-gradient(circle at 45% 40%, var(--photo-light), var(--photo-dark));
    border: 6px solid var(--white);
    box-shadow: 0 0 0 9px var(--ring);
  }
  .brand {
    position: absolute; left: 29px; top: 118px; width: 235px;
    text-align: center; color: var(--ink);
  }
  .brand__name { font-size: 52px; font-weight: 700; line-height: 1; letter-spacing: 1px; }
  .brand__tag { font-size: 20px; font-weight: 400; margin-top: 2px; letter-spacing: 1px; }
  .brand-square {
    position: absolute; left: 12px; top: 245px;
    width: 221px; height: 211px;
    background: var(--ink);
    box-shadow: inset 0 0 0 12px var(--ink), inset 0 0 0 15px var(--white);
  }
  .offer {
    position: absolute; left: 384px; top: 74px;
    color: var(--white); font-weight: 700; font-size: 16px; line-height: 24px;
  }
  .service { position: absolute; display: flex; gap: 10px; color: var(--white); font-weight: 700; }
  .service__arrow { width: 22px; height: 20px; flex: none; }
  .service--main { left: 358px; top: 150px; line-height: 36px; }
  .service--main .service__arrow { margin-top: 9px; }
  .service__title { font-size: 34px; }
  .service__note { font-size: 20px; }
  .service--list { left: 286px; top: 245px; font-size: 23px; line-height: 26px; }
  .service--list .service__arrow { margin-top: 3px; }
  .url {
    position: absolute; left: 360px; top: 405px;
    color: var(--white); font-weight: 700; font-size: 16px;
  }
  .footer-name {
    position: absolute; left: 281px; top: 457px;
    color: var(--ink); font-weight: 700; font-size: 16px;
  }
</style>
</head>
<body>
  <main class="cover">
    <div class="top-band">
      <div class="top-band__brand"><span class="top-band__square"></span>VELTRA CONSULTORIA</div>
    </div>

    <svg class="panel" viewBox="0 0 1061 401" aria-hidden="true">
      <defs>
        <linearGradient id="panelFill" x1="0" y1="0" x2="1" y2="0">
          <stop offset="0" stop-color="#0e3a68"/>
          <stop offset="0.55" stop-color="#2a679d"/>
          <stop offset="1" stop-color="#0e3a68"/>
        </linearGradient>
      </defs>
      <path d="M365 0 H1061 V401 H257 C275 280 300 110 365 0 Z" fill="url(#panelFill)"/>
      <path d="M365 0 C300 110 275 280 257 401" fill="none" stroke="#0a2a4d" stroke-width="9"/>
    </svg>

    <div class="photo" role="img" aria-label="Foto de reunião de negócios: apresentador de terno diante de uma equipe sentada"></div>

    <div class="brand">
      <div class="brand__name">VELTRA</div>
      <div class="brand__tag">CONSULTORIA</div>
    </div>
    <div class="brand-square"></div>

    <p class="offer">A VELTRA oferece serviços de consultoria empresarial<br>para empresas em todo o país nas seguintes áreas:</p>

    <div class="service service--main">
      <svg class="service__arrow" viewBox="0 0 26 24"><path d="M0 0 L26 12 L0 24 L7 12 Z" fill="#ffffff"/></svg>
      <div><span class="service__title">SEGUROS</span> <span class="service__note">(GESTÃO TÉCNICA,<br>COMERCIAL E OPERACIONAL)</span></div>
    </div>
    <div class="service service--list">
      <svg class="service__arrow" viewBox="0 0 26 24"><path d="M0 0 L26 12 L0 24 L7 12 Z" fill="#ffffff"/></svg>
      <div>TREINAMENTO-PLANO DE NEGÓCIOS<br>GESTÃO DE OPERAÇÕES<br>PLANEJAMENTO ESTRATÉGICO<br>GESTÃO ECONÔMICA - GESTÃO DE<br>MARKETING</div>
    </div>

    <p class="url">WWW.VELTRACONSULTORIA.COM.BR</p>
    <p class="footer-name">VELTRA CONSULTORIA</p>
  </main>
</body>
</html>
```